The Wardrobe Sage needs a business card

The wardrobe sage is a lead generation service serving the Custom Closet industry.

Here is the basic card information:

The Wardrobe Sage
Dorian Pettigrew
Owner/CEO
Harlow Bend, NC
704-318-5527 Cell
Email: dpettigrew@TheWardrobeSage.com

Additional information for the card:

"High quality, flat rate lead generation exclusively for the custom closet industry"

Bullet points for the back:

- Low fixed cost
- Easy to budget
- Guaranteed qualified Leeds
- Exclusivity per city

Logo attached, head shot attached. Photos of closet systems attached

```html
<!DOCTYPE html>
<html lang="en">
<head>
<meta charset="utf-8">
<title>The Wardrobe Sage – Business Card</title>
<link href="https://fonts.googleapis.com/css2?family=Crimson+Text:wght@400;600&family=Great+Vibes&family=Montserrat:wght@300&family=Poppins:wght@400&display=swap" rel="stylesheet">
<style>
  :root {
    --page: #e2e2e2;
    --card: #ffffff;
    --charcoal: #2e2e33;
    --charcoal-soft: #3a3a40;
    --bronze: #a8622e;
    --ink: #3b3b3f;
    --grey: #8d8d92;
    --white: #ffffff;
  }
  * { box-sizing: border-box; margin: 0; padding: 0; }
  html, body { width: 759px; height: 1200px; overflow: hidden; }
  body { background: var(--page); position: relative; }

  .card {
    position: absolute;
    top: 302px;
    width: 340px;
    height: 595px;
    background: var(--card);
    overflow: hidden;
    box-shadow: 0 8px 18px rgba(0,0,0,.28);
  }
  .card--front { left: 26px; }
  .card--back { left: 393px; }

  .dark-band {
    position: absolute; left: 0; right: 0; bottom: 0;
    background: linear-gradient(180deg, var(--charcoal-soft) 0%, var(--charcoal) 100%);
  }
  .card--front .dark-band { top: 356px; }
  .card--back .dark-band { top: 302px; }

  .brand-name {
    position: absolute; left: 0; right: 0;
    text-align: center;
    font-family: "Crimson Text", serif;
    font-weight: 600;
    font-size: 34px;
    line-height: 1.05;
    color: var(--bronze);
  }
  .card--front .brand-name { top: 104px; }
  .card--back .brand-name { top: 122px; }

  .photo {
    position: absolute;
    width: 119px; height: 73px;
    border: 2px solid #d9c3b0;
  }
  .photo--a { left: 53px; top: 184px; background: linear-gradient(135deg, #b86a45, #6b3a26 70%, #d8c9a8); }
  .photo--b { left: 182px; top: 184px; background: linear-gradient(135deg, #9fb6d6, #d7dde6 60%, #6f757d); }
  .photo--c { left: 182px; top: 266px; background: linear-gradient(135deg, #e8e3de, #b78ea0 55%, #5d6c8c); }
  .photo--d { left: 182px; top: 346px; background: linear-gradient(135deg, #3d3530, #e6e2dc 60%, #8b8580); }

  .headshot {
    position: absolute; left: 39px; top: 292px;
    width: 128px; height: 128px; border-radius: 50%;
    border: 5px solid var(--bronze);
    background: radial-gradient(circle at 50% 45%, #5a5654, #2a2a2e 75%);
  }

  .person-name {
    position: absolute; left: 42px; top: 424px;
    font-family: "Great Vibes", cursive;
    font-size: 38px;
    line-height: 44px;
    color: var(--bronze);
  }
  .person-role {
    position: absolute; left: 43px; top: 459px;
    font-family: "Montserrat", sans-serif;
    font-weight: 300;
    font-size: 18px;
    letter-spacing: 3.5px;
    color: var(--grey);
  }
  .contact-list {
    position: absolute; left: 44px; top: 488px;
    list-style: none;
    font-family: "Poppins", sans-serif;
    font-size: 14px;
    color: var(--white);
  }
  .contact-list li { display: flex; align-items: center; height: 23px; white-space: nowrap; }
  .contact-list svg { width: 13px; height: 13px; margin-right: 7px; flex: none; }

  .tagline {
    position: absolute; left: 0; right: 0; top: 196px;
    text-align: center;
    font-family: "Great Vibes", cursive;
    font-size: 27px;
    line-height: 21px;
    color: var(--bronze);
  }
  .tagline-caps {
    position: absolute; left: 0; right: 0; top: 240px;
    text-align: center;
    font-family: "Crimson Text", serif;
    font-size: 15px;
    line-height: 19px;
    color: var(--ink);
  }

  .benefit {
    position: absolute; width: 130px;
    text-align: center;
    font-family: "Crimson Text", serif;
    font-size: 18px;
    line-height: 20px;
    color: var(--white);
  }
  .benefit-icon {
    display: block; margin: 0 auto 8px;
    width: 44px; height: 44px; border-radius: 50%;
    background: var(--white);
  }
  .benefit--1 { left: 30px; top: 336px; }
  .benefit--2 { left: 176px; top: 336px; }
  .benefit--3 { left: 30px; top: 449px; }
  .benefit--4 { left: 176px; top: 449px; }
</style>
</head>
<body>

<section class="card card--front">
  <div class="dark-band"></div>
  <div class="brand-name">The Wardrobe Sage</div>

  <div class="photo photo--a" role="img" aria-label="Photo of a custom garage cabinet system in copper finish"></div>
  <div class="photo photo--b" role="img" aria-label="Photo of a laundry and mudroom storage system"></div>
  <div class="photo photo--c" role="img" aria-label="Photo of a walk-in closet with shelving and chandelier"></div>
  <div class="photo photo--d" role="img" aria-label="Photo of a home office with built-in cabinetry"></div>

  <div class="headshot" role="img" aria-label="Headshot of the owner"></div>

  <div class="person-name">Dorian Pettigrew</div>
  <div class="person-role">OWNER/CEO</div>
  <ul class="contact-list">
    <li>
      <svg viewBox="0 0 12 12"><path d="M6 0.5a4 4 0 0 1 4 4c0 3-4 7-4 7s-4-4-4-7a4 4 0 0 1 4-4z" fill="#a8622e"/><circle cx="6" cy="4.5" r="1.5" fill="#2e2e33"/></svg>
      Harlow Bend, NC
    </li>
    <li>
      <svg viewBox="0 0 12 12"><path d="M2.5 1l2 0.3 0.8 2.4-1.3 1a7 7 0 0 0 3.3 3.3l1-1.3 2.4 0.8 0.3 2c-5.5 0.8-9.3-3-8.5-8.5z" fill="#a8622e"/></svg>
      704-318-5527
    </li>
    <li>
      <svg viewBox="0 0 12 12"><rect x="0.5" y="2" width="11" height="8" fill="#a8622e"/><path d="M0.5 2.5l5.5 4 5.5-4" fill="none" stroke="#2e2e33" stroke-width="1"/></svg>
      dpettigrew@TheWardrobeSage.com
    </li>
  </ul>
</section>

<section class="card card--back">
  <div class="dark-band"></div>
  <div class="brand-name">The Wardrobe Sage</div>

  <p class="tagline">High quality, flat<br>rate lead generation</p>
  <p class="tagline-caps">EXCLUSIVELY FOR THE CUSTOM<br>CLOSET INDUSTRY.</p>

  <div class="benefit benefit--1">
    <svg class="benefit-icon" viewBox="0 0 44 44"><circle cx="22" cy="22" r="22" fill="#fff"/><circle cx="22" cy="17" r="6" fill="none" stroke="#3b3b3f" stroke-width="1.2"/><text x="22" y="20" text-anchor="middle" font-size="8" fill="#3b3b3f" font-family="serif">$</text><path d="M16 26v7m-2-2l2 2 2-2M22 26v8m-2-2l2 2 2-2M28 26v7m-2-2l2 2 2-2" fill="none" stroke="#3b3b3f" stroke-width="1.2"/></svg>
    Low fixed<br>cost
  </div>
  <div class="benefit benefit--2">
    <svg class="benefit-icon" viewBox="0 0 44 44"><circle cx="22" cy="22" r="22" fill="#fff"/><circle cx="24" cy="16" r="5" fill="none" stroke="#3b3b3f" stroke-width="1.2"/><text x="24" y="19" text-anchor="middle" font-size="7" fill="#3b3b3f" font-family="serif">$</text><path d="M11 29h6l5 2h6l5-4M11 29v4h6l6 1 10-6" fill="none" stroke="#3b3b3f" stroke-width="1.2"/></svg>
    Easy to<br>budget
  </div>
  <div class="benefit benefit--3">
    <svg class="benefit-icon" viewBox="0 0 44 44"><circle cx="22" cy="22" r="22" fill="#fff"/><path d="M22 10l9 3v7c0 6-4 10-9 12-5-2-9-6-9-12v-7z" fill="none" stroke="#3b3b3f" stroke-width="1.3"/><path d="M18 21h3l1-4 2 1-1 3h3v5h-8z" fill="none" stroke="#3b3b3f" stroke-width="1.1"/></svg>
    Guaranteed<br>qualified Leeds
  </div>
  <div class="benefit benefit--4">
    <svg class="benefit-icon" viewBox="0 0 44 44"><circle cx="22" cy="22" r="22" fill="#fff"/><circle cx="22" cy="18" r="7" fill="none" stroke="#3b3b3f" stroke-width="1.3"/><path d="M22 14.5l1.1 2.3 2.4.3-1.8 1.7.5 2.4-2.2-1.2-2.2 1.2.5-2.4-1.8-1.7 2.4-.3z" fill="#3b3b3f"/><path d="M18 24l-3 8 3-1 2 3 2-6M26 24l3 8-3-1-2 3-2-6" fill="none" stroke="#3b3b3f" stroke-width="1.2"/></svg>
    Exclusivity<br>per city
  </div>
</section>

</body>
</html>
```